Rehearsal studio business card design needed

My rehearsal studio i bought not that long ago was opened as a hobby originally and was definitely not taken seriously. I am trying to make the new look studio be launched with the new look business cards. I am looking for very simple and clean look cards to match the simple and clean studios. the colour scheme is red and grey. over all i am really just looking for a very simple card that is not too busy and just gets the point accross.
Target Market(s)
Targeting bands, music teachers, students, etc.
Industry/Entity Type
Business
Contact Information for Business Card
Bayridge Sound Centre
Rehearsal and Recording Facilities
Owen Barlow CEO
unit 8, 47 Garvin Road Tallow NSW 2093
0491 382 905
bayridgesoundcentre@mailvex.com
Requirements
Must have
- simplicity
Nice to have

```html
<!DOCTYPE html>
<html lang="en">
<head>
<meta charset="utf-8">
<title>Bayridge Sound Centre – Business Card</title>
<link rel="stylesheet" href="https://fonts.googleapis.com/css2?family=Exo+2:wght@400;600&display=swap">
<style>
  :root {
    --page-bg: #2b2b2d;
    --card-bg: #15161c;
    --brand-red: #c8202b;
    --text-grey: #b9b9bc;
    --name-light: #e6e6e8;
    --meter-grey: #7a7a7e;
    --meter-dark: #4e4e52;
  }
  * { margin: 0; padding: 0; box-sizing: border-box; }
  html, body { width: 1200px; height: 900px; overflow: hidden; }
  body {
    background: var(--page-bg);
    font-family: "Exo 2", sans-serif;
    position: relative;
  }
  .card {
    position: absolute;
    left: 250px;
    width: 700px;
    height: 400px;
    background: var(--card-bg);
    border-radius: 26px;
    box-shadow: 0 10px 30px rgba(0,0,0,0.45);
    overflow: hidden;
  }
  .card--back { top: 36px; }
  .card--front { top: 464px; }

  /* Back side */
  .back-mark {
    position: absolute;
    inset: 0;
    display: flex;
    align-items: center;
    justify-content: center;
    gap: 22px;
  }
  .back-mark__dot {
    width: 70px; height: 70px;
    border-radius: 50%;
    background: var(--brand-red);
  }
  .back-mark__name {
    color: var(--name-light);
    font-weight: 600;
    font-size: 40px;
    letter-spacing: 1px;
  }

  /* Front side */
  .front-name {
    position: absolute;
    top: 62px; left: 0; right: 0;
    text-align: center;
    color: var(--name-light);
    font-weight: 600;
    font-size: 46px;
    letter-spacing: 1px;
  }
  .contact {
    position: absolute;
    top: 170px; left: 0; right: 0;
    text-align: center;
    font-size: 17px;
    line-height: 1.3;
    color: var(--text-grey);
  }
  .contact__company, .contact__tagline {
    color: var(--brand-red);
    font-weight: 600;
  }
  .contact__phone {
    color: var(--brand-red);
    font-size: 20px;
    margin-top: 16px;
  }
  .contact__email { margin-top: 10px; font-size: 18px; }

  .level-meter {
    position: absolute;
    width: 140px;
    height: 80px;
    border-radius: 3px;
    background: linear-gradient(to bottom, var(--brand-red) 0%, var(--meter-grey) 35%, var(--meter-dark) 100%);
  }
  .level-meter--left { left: 40px; bottom: 40px; }
  .level-meter--right { right: 40px; top: 160px; }
</style>
</head>
<body>

<section class="card card--back" aria-label="Card back">
  <div class="back-mark">
    <span class="back-mark__dot"></span>
    <span class="back-mark__name">Bayridge Sound Centre</span>
  </div>
</section>

<section class="card card--front" aria-label="Card front">
  <div class="front-name">Bayridge Sound Centre</div>

  <div class="contact">
    <div class="contact__company">Bayridge Sound Centre</div>
    <div class="contact__tagline">Rehearsal and Recording Facilities</div>
    <div>Owen Barlow CEO unit 8,</div>
    <div>47 Garvin Road Tallow NSW 2093</div>
    <div class="contact__phone">0491 382 905</div>
    <div class="contact__email">bayridgesoundcentre@mailvex.com</div>
  </div>

  <div class="level-meter level-meter--left" role="img" aria-label="Audio level meter graphic in red and grey"></div>
  <div class="level-meter level-meter--right" role="img" aria-label="Audio level meter graphic in red and grey"></div>
</section>

</body>
</html>
```